Need a landing page design updated

Need an existing landing page perfected, want it too look similar to one of Quenbrook's landing pages in that it flows and is really aesthetically pleasing. The link to the landing page is below. I need this design updated asap. Please take the content directly from the page.

http://verdanthollowsx.com/residential-services/

Target Market(s)

High end residential landscape customers on the gulf coast of Florida (Clearwater area)

Industry/Entity Type

Landscape Gardening

Font styles to use
Sans Serif
Decorative

Requirements
Must have
• I want to keep the written content the same on on the landing page, but would like to work on making both aesthetically appealing to the consumer. This is for high end residential clients on the gulf coast of florida, so think palm trees and sunny beaches with beautiful houses and gorgeous landscapes....look through www.verdanthollowsx.com home page for an example of the houses we landscape.
Nice to have
• Would like it to flow as you scroll similar to Quenbrook's landing pages.
• Look at how Quenbrook's landing page flows, want similar here.....
• https://www.quenbrook.com/tavlo-q/
Should not have
• this landing page must be beautiful and must make a lot of sense as you scroll, am looking for a work of art....please do not submit generic templates or anything that can be easily done....I need real artistry.

```html
<!DOCTYPE html>
<html lang="en">
<head>
<meta charset="utf-8">
<title>Verdant Hollow — Residential Landscaping</title>
<link rel="stylesheet" href="https://fonts.googleapis.com/css2?family=Mulish:wght@300;400;600;700;800&display=swap">
<style>
:root{
  --teal:#1aa6c2;
  --teal-dark:#0f8aa6;
  --blue:#1d8bd3;
  --blue-deep:#1670b4;
  --ink:#3d4a52;
  --muted:#6d7880;
  --white:#ffffff;
  --panel:#2f3b3f;
}
*{box-sizing:border-box;margin:0;padding:0}
html,body{width:1200px;height:4344px;overflow:hidden}
body{font-family:"Mulish",sans-serif;color:var(--ink);background:var(--white)}
section,header,footer{position:relative;width:1200px;overflow:hidden}
.photo{position:absolute}

/* header */
.site-header{height:110px;background:var(--white)}
.brand{position:absolute;left:40px;top:20px;display:flex;align-items:center;gap:10px;font-size:28px;font-weight:800;color:var(--teal);letter-spacing:1px}
.brand-dot{width:18px;height:18px;border-radius:50%;background:var(--teal)}
.contact{position:absolute;right:40px;top:22px;text-align:right;font-size:13px;color:var(--muted);line-height:1.5}
.contact b{color:var(--teal)}
.nav{position:absolute;left:0;top:74px;width:100%;height:36px;background:var(--teal);display:flex;gap:28px;padding-left:40px;align-items:center}
.nav a{color:var(--white);font-size:13px;font-weight:700;text-decoration:none;letter-spacing:.5px}

/* hero */
.hero{height:510px}
.hero .photo{inset:0;background:linear-gradient(180deg,#9ec7e0 0%,#c9d9d4 30%,#5f8a4a 62%,#3f6d2f 100%)}
.hero .photo::after{content:"";position:absolute;right:0;bottom:40px;width:560px;height:140px;background:linear-gradient(90deg,rgba(214,40,110,0) 0%,rgba(214,40,110,.55) 60%,rgba(230,70,130,.7) 100%);border-radius:80px 0 0 80px}
.hero-text{position:absolute;left:60px;top:260px;width:600px;font-size:27px;line-height:1.35;color:var(--white);font-weight:400;text-shadow:0 2px 8px rgba(0,0,0,.35)}

/* intro */
.intro{height:480px;text-align:center}
.palm-left{left:0;top:50px;width:190px;height:300px;background:linear-gradient(120deg,rgba(80,130,70,.55) 0%,rgba(140,170,110,.3) 60%,rgba(255,255,255,0) 100%);border-radius:0 40px 40px 0}
.palm-right{right:0;top:40px;width:200px;height:340px;background:linear-gradient(240deg,rgba(80,130,70,.55) 0%,rgba(140,170,110,.3) 60%,rgba(255,255,255,0) 100%);border-radius:40px 0 0 40px}
.intro h2{padding-top:110px;font-size:34px;font-weight:600;line-height:1.3;color:var(--ink)}
.intro p{width:620px;margin:26px auto 0;font-size:16px;line-height:1.6;color:var(--muted)}
.intro .right{display:block;margin-top:18px;color:var(--teal);font-weight:700;font-size:17px}

/* services */
.services{height:480px}
.services .photo{inset:0;background:linear-gradient(180deg,#3a8fd8 0%,#69b3e6 40%,#a9d7ea 62%,#e9dfc6 82%,#e3d3b2 100%)}
.services .lead{position:relative;text-align:center;color:var(--white);padding-top:42px}
.services .lead small{display:block;font-size:19px;font-weight:400}
.services .lead h2{width:760px;margin:14px auto 0;font-size:29px;font-weight:600;line-height:1.3}
.service-boxes{position:absolute;left:105px;top:175px;display:flex;gap:40px}
.service-box{width:475px;height:240px;background:rgba(47,59,63,.82);color:var(--white);padding:26px 30px}
.service-box h3{font-size:17px;font-weight:700;margin-bottom:14px}
.service-box p{font-size:11.5px;line-height:1.5;color:#d9e1e4;margin-bottom:10px;padding-left:10px}

/* care */
.care{height:440px;margin-top:20px}
.care-text{position:absolute;left:100px;top:50px;width:440px}
.care-text h2{font-size:22px;font-weight:600;line-height:1.4;color:var(--ink)}
.care-text p{font-size:13px;line-height:1.6;color:var(--muted);margin-top:16px}
.care .photo{left:600px;top:0;width:600px;height:440px;background:linear-gradient(180deg,#2d7fd0 0%,#5fa8e2 45%,#f0f1ee 46%,#e5e8e3 70%,#4f8a3d 86%,#3e6e30 100%)}

/* disturb */
.disturb{height:460px}
.disturb .photo{left:0;top:0;width:600px;height:460px;background:linear-gradient(180deg,#3b90d8 0%,#7cbbe6 35%,#f4f3ef 36%,#e6e4dc 78%,#6f9c55 100%)}
.disturb-panel{position:absolute;left:600px;top:0;width:600px;height:460px;background:linear-gradient(160deg,var(--blue) 0%,var(--blue-deep) 100%);color:var(--white);padding:170px 80px 0 60px}
.disturb-panel h2{font-size:22px;font-weight:600;line-height:1.4}
.disturb-panel p{font-size:13px;line-height:1.55;margin-top:14px;color:#dcecf8}

/* benefits */
.benefits{height:480px}
.benefits .photo{inset:0;background:linear-gradient(180deg,#6aa8d8 0%,#a9cde6 35%,#dfe6e0 55%,#7ea065 78%,#4f7a3e 100%)}
.benefits h2{position:relative;text-align:center;padding-top:50px;font-size:32px;font-weight:600;line-height:1.25;color:var(--ink)}
.benefit-cards{position:absolute;left:130px;top:210px;display:flex;gap:50px}
.benefit-card{position:relative;width:280px;height:170px;background:var(--white);border:3px solid var(--teal);border-radius:12px;padding:56px 24px 0;text-align:center;font-size:13px;line-height:1.5;color:var(--ink)}
.benefit-icon{position:absolute;left:50%;top:-36px;margin-left:-36px;width:72px;height:72px;border-radius:50%;background:var(--teal);border:5px solid var(--white);display:flex;align-items:center;justify-content:center}

/* testimonials */
.testimonials{height:440px}
.testimonials-text{position:absolute;left:100px;top:40px;width:450px}
.testimonials-text h2{font-size:22px;font-weight:600;line-height:1.4;color:var(--teal)}
.testimonials-text p{font-size:13px;line-height:1.6;color:var(--muted);margin-top:14px}
.testimonials .photo{left:600px;top:0;width:600px;height:440px;background:linear-gradient(180deg,#4a96d6 0%,#8cc2e6 40%,#f2f2ef 41%,#e2e2dc 75%,#5e8d47 100%)}

/* flaws */
.flaws{height:360px;text-align:center;color:var(--white)}
.flaws .photo{inset:0;background:linear-gradient(180deg,#3a3430 0%,#5a4a3c 45%,#6b5a45 70%,#47402f 100%)}
.flaws-inner{position:relative;padding-top:70px}
.flaws h2{font-size:32px;font-weight:600}
.flaws h3{font-size:19px;font-weight:600;color:#8fdff0;margin-top:10px}
.flaws p{font-size:15px;margin-top:10px}

/* cta */
.cta{height:460px;text-align:center}
.cta .photo{inset:0;background:
  linear-gradient(90deg,rgba(70,130,65,.75) 0%,rgba(120,160,90,.35) 14%,rgba(255,255,255,0) 26%,rgba(255,255,255,0) 74%,rgba(120,160,90,.35) 86%,rgba(70,130,65,.75) 100%),
  linear-gradient(180deg,#ece6d0 0%,#f3efdd 55%,#9cc8dc 100%)}
.cta-inner{position:relative;padding-top:60px}
.cta h2{font-size:29px;font-weight:600;line-height:1.3;color:var(--ink)}
.cta p{font-size:16px;margin-top:14px;color:var(--ink)}
.cta-form{width:480px;margin:70px auto 0;background:var(--teal);padding:22px 28px 26px;border-radius:4px}
.cta-fields{display:flex;gap:16px}
.cta-field{flex:1;height:32px;background:var(--white);border-radius:2px;font-size:12px;color:var(--muted);text-align:left;padding:8px 10px}
.cta-button{display:block;margin:16px auto 0;width:100%;height:38px;background:var(--teal-dark);color:var(--white);font-size:16px;font-weight:700;border:0;font-family:inherit;border-radius:2px}

/* footer */
.site-footer{height:104px;background:var(--teal);color:var(--white);font-size:14px;text-align:center;padding-top:44px}
</style>
</head>
<body>

<header class="site-header">
  <div class="brand"><span class="brand-dot"></span>VERDANT HOLLOW</div>
  <div class="contact">Call Us Now on: <b>(555) 014-2278</b><br>Client Portal | Get A Free Quote</div>
  <nav class="nav"><a>HOME</a><a>ABOUT US</a><a>RESIDENTIAL</a><a>COMMERCIAL</a><a>BLOG</a><a>CONTACT US</a></nav>
</header>

<section class="hero">
  <div class="photo" role="img" aria-label="Sunny front garden of a white house with green lawn and pink flower beds"></div>
  <p class="hero-text">You don't have an abundance of free time. And, you simply don't want to spend the little time you have – mowing a lawn and pruning the plants.</p>
</section>

<section class="intro">
  <div class="photo palm-left" role="img" aria-label="Palm tree photo"></div>
  <div class="photo palm-right" role="img" aria-label="Palm tree photo"></div>
  <h2>You would probably like to spend that time<br>the way you should, instead.</h2>
  <p>Enjoying the sunset in the privacy of your garden, watching a favorite TV show while lying on a hammock, or throwing an occasional BBQ party with your friends and loved ones<span class="right">Right?</span></p>
</section>

<section class="services">
  <div class="photo" role="img" aria-label="Blue sky over a sunny sandy beach"></div>
  <div class="lead">
    <small>Getting an outdoor area of your dreams is not that difficult, nor expensive.</small>
    <h2>You can make this happen by getting a help from a landscaping company that offers tailor-made services.</h2>
  </div>
  <div class="service-boxes">
    <div class="service-box">
      <h3>Generic Landscaping Services:</h3>
      <p>You pay for the bundle of services, regardless of whether you actually need them.</p>
      <p>You get a general service not customised for the specific needs of your outdoor area.</p>
      <p>No one takes real notice of your property, or checks what is best to maintain.</p>
    </div>
    <div class="service-box">
      <h3>Tailor-made landscaping services:</h3>
      <p>You pay only for the services your yard really needs.</p>
      <p>You get plant-specific routine maintenance and care as requirements vary.</p>
      <p>We focus each detail on your taste and on improving your property.</p>
    </div>
  </div>
</section>

<section class="care">
  <div class="care-text">
    <h2>Why should you care that Verdant Hollow employs the leading industry experts and uses modern, eco-friendly technical solutions?</h2>
    <p>That is why we're able to transform your lawn into a green carpet and get your plants in a perfect health. All while keeping your vision and your budget on our minds.</p>
    <p>That is why our services actually enable you to reduce the operating expenses.</p>
  </div>
  <div class="photo" role="img" aria-label="White coastal villa with palm trees under a blue sky"></div>
</section>

<section class="disturb">
  <div class="photo" role="img" aria-label="White two-storey house with porch and front lawn"></div>
  <div class="disturb-panel">
    <h2>Do you worry our services are going to disturb you while trying to unwind in the privacy of your own garden?</h2>
    <p>Our Client Service Operators Build A Schedule Around Your Needs - Designed Not To Disturb You At All.</p>
  </div>
</section>

<section class="benefits">
  <div class="photo" role="img" aria-label="Palm-lined residential garden in soft light"></div>
  <h2>More Benefits of<br>Having a Well-maintained yard:</h2>
  <div class="benefit-cards">
    <div class="benefit-card">
      <div class="benefit-icon"><svg width="32" height="32" viewBox="0 0 32 32" fill="none" stroke="#fff" stroke-width="2.5" stroke-linecap="round" stroke-linejoin="round"><path d="M4 26h24"/><path d="M6 21l7-7 5 5 9-10"/><path d="M22 9h5v5"/></svg></div>
      In some cases, a great-looking lawn can increase your property's value up to 20%.
    </div>
    <div class="benefit-card">
      <div class="benefit-icon"><svg width="32" height="32" viewBox="0 0 32 32" fill="none" stroke="#fff" stroke-width="2.5" stroke-linecap="round" stroke-linejoin="round"><path d="M8 26C8 14 16 6 27 5c0 12-7 19-17 19"/><path d="M8 26l10-10"/></svg></div>
      Your lawn and plants reduce the energy consumption – countering the warming effects of paved surfaces.
    </div>
    <div class="benefit-card">
      <div class="benefit-icon"><svg width="32" height="32" viewBox="0 0 32 32" fill="none" stroke="#fff" stroke-width="2.5" stroke-linecap="round" stroke-linejoin="round"><path d="M26 12a11 11 0 0 0-19-3"/><path d="M6 4v5h5"/><path d="M6 20a11 11 0 0 0 19 3"/><path d="M26 28v-5h-5"/></svg></div>
      They act as giant dust filters, increasing air quality, and removing carbon dioxide from the atmosphere
    </div>
  </div>
</section>

<section class="testimonials">
  <div class="testimonials-text">
    <h2>At Verdant Hollow, we do more than just keeping your landscape in a pristine state.</h2>
    <p>This is what some of our long-term clients say about our approach:</p>
    <p>"We are delighted with your landscaping. Both with the design and implementation of it; not very often these days that work exceeds expectations!"</p>
    <p>"Verdant Hollow are efficient, on-time, responsive, provide fair pricing, do outstanding work, have great people, and actually follow up on their word!"</p>
  </div>
  <div class="photo" role="img" aria-label="Modern white villa framed by tall palm trees"></div>
</section>

<section class="flaws">
  <div class="photo" role="img" aria-label="Evening garden terrace in warm shadowed tones"></div>
  <div class="flaws-inner">
    <h2>Do our services have flaws?</h2>
    <h3>Yes. They have two giant ones:</h3>
    <p>1. Your new garden will get all your neighbors jealous.</p>
    <p>2. Your friends will probably start inviting themselves over more frequently.</p>
  </div>
</section>

<section class="cta">
  <div class="photo" role="img" aria-label="Bright beach framed by palm fronds"></div>
  <div class="cta-inner">
    <h2>So, what's the next step to enriching your living area?<br>And getting you a garden from your dreams.</h2>
    <p>It's simple, just book a no-obligations consultation</p>
    <form class="cta-form">
      <div class="cta-fields"><div class="cta-field">Name</div><div class="cta-field">Email Address</div></div>
      <button class="cta-button" type="button">Get Started</button>
    </form>
  </div>
</section>

<footer class="site-footer">Copyright 2017 Verdant Hollow All Rights Reserved.</footer>

</body>
</html>
```